Corvath Properties Business Card Design

We would now like to design business cards with the new Corvath Properties logo

Target Market(s)

Professional

Industry/Entity Type

Professional services

Contact Information for Business Card

Employee name, title, phone number, email address, corporate office address and logo.

Font styles to use
Sans Serif

Colors
0054AA
0677BA
7BADD7
CADEEF
E8F1F8

Requirements
Must have
• My logo
Should not have
• any other pictures or images besides my logo

```html
<!DOCTYPE html>
<html lang="en">
<head>
<meta charset="utf-8">
<title>Corvath Properties Business Card</title>
<link href="https://fonts.googleapis.com/css2?family=Montserrat:wght@400;600&display=swap" rel="stylesheet">
<style>
  :root {
    --brand-blue: #367cc0;
    --ink: #2b2b2b;
    --paper: #ffffff;
    --backdrop: #ebebeb;
  }
  html, body {
    margin: 0;
    padding: 0;
    width: 1200px;
    height: 1028px;
    overflow: hidden;
    background: var(--backdrop);
    font-family: "Montserrat", Arial, sans-serif;
  }
  .canvas {
    position: relative;
    width: 1200px;
    height: 1028px;
  }
  .card {
    position: absolute;
    left: 310px;
    width: 579px;
    height: 331px;
    border-radius: 24px;
    box-sizing: border-box;
  }
  .card-front {
    top: 165px;
    background: var(--paper);
    color: var(--ink);
  }
  .card-back {
    top: 532px;
    background: var(--brand-blue);
    display: flex;
    align-items: center;
    justify-content: center;
  }
  .person-name {
    position: absolute;
    left: 42px;
    top: 39px;
    margin: 0;
    font-size: 20px;
    font-weight: 600;
    color: var(--brand-blue);
  }
  .person-title {
    position: absolute;
    left: 42px;
    top: 65px;
    margin: 0;
    font-size: 14px;
    font-weight: 400;
    letter-spacing: 0.3px;
  }
  .website {
    position: absolute;
    right: 42px;
    top: 65px;
    margin: 0;
    font-size: 14px;
    letter-spacing: 0.4px;
  }
  .divider {
    position: absolute;
    left: 42px;
    right: 42px;
    top: 101px;
    height: 0;
    border-top: 1px solid var(--brand-blue);
  }
  .contact {
    position: absolute;
    left: 42px;
    top: 200px;
    font-size: 14px;
    line-height: 20px;
    letter-spacing: 0.3px;
  }
  .contact-row {
    display: flex;
    align-items: center;
    gap: 9px;
  }
  .contact-row svg {
    width: 12px;
    height: 12px;
    flex: none;
  }
  .address {
    margin: 10px 0 0;
    font-style: normal;
  }
  .brand-name {
    margin: 0;
    font-weight: 600;
    text-transform: uppercase;
    line-height: 1.05;
  }
  .brand-name-front {
    position: absolute;
    right: 42px;
    top: 176px;
    width: 170px;
    text-align: right;
    font-size: 30px;
    color: var(--brand-blue);
  }
  .brand-name-back {
    font-size: 54px;
    color: var(--paper);
    text-align: left;
  }
</style>
</head>
<body>
<main class="canvas">
  <section class="card card-front" aria-label="Card front">
    <h1 class="person-name">Lena Marsh</h1>
    <p class="person-title">Director</p>
    <p class="website">www.corvathproperties.com</p>
    <div class="divider"></div>

    <div class="contact">
      <div class="contact-row">
        <svg viewBox="0 0 12 12" aria-hidden="true">
          <path d="M3 1 L4.6 3.4 L3.6 4.5 C4.3 6.2 5.6 7.6 7.4 8.4 L8.5 7.4 L11 9 L10 11 C5.5 10.6 1.4 6.5 1 2 Z" fill="var(--brand-blue)"/>
        </svg>
        <span>(555) 014-2286</span>
      </div>
      <div class="contact-row">
        <svg viewBox="0 0 12 12" aria-hidden="true">
          <rect x="0.8" y="2.3" width="10.4" height="7.4" fill="none" stroke="var(--brand-blue)" stroke-width="1.2"/>
          <path d="M1 2.6 L6 6.4 L11 2.6" fill="none" stroke="var(--brand-blue)" stroke-width="1.2"/>
        </svg>
        <span>info@corvathproperties.com</span>
      </div>
      <address class="address">418 Ridgeline Court<br>Salem, OR 97301</address>
    </div>

    <p class="brand-name brand-name-front">Corvath<br>Properties</p>
  </section>

  <section class="card card-back" aria-label="Card back">
    <p class="brand-name brand-name-back">Corvath<br>Properties</p>
  </section>
</main>
</body>
</html>
```